Professional and modern website for Real Estate services company

Hi there! We're looking for a responsive, highly professional and modern (in line with Latest trends) coded website for a Real Estate services company named Portalia720º (find logo attached). I will try to Explain how I picture it in my head, but feel free to step out of the script and design it as you please. The structure for the website must be as Follows: - Menu: at the top of the screen, always visible (in any page and when to scrolling down). Logo at the left hand side (clicking redirects to home), then a Services, About us, Blog and Contact and on the right hand, Estimate and Log in (just placeholder, no log in required yet). - Home: (I like https://fr.domvera.example/): a landscape picture of Madrid's skyline. Very important That at a first glance (without scrolling) you can see a box to input data of your building to get an estimate (Post code, Number of homes, Number of garages, Number of stores, Swimming pool (yes / no) Concierge (yes / no)). Should there be a small space Also for a corporate presentation video (more or less like https://www.velbrastahogares.example/ but With the estimate Request box INSTEAD OF the App - however, do not take this one as example Given I just wanted to illustrate the structure). Still in the Home, bellow the first glance, I'd like to have a brief introduction of the following pages (Services, About us, Blog and Contact). This can be in a Either "square" form (like https://fr.domvera.example/) or in a "scroll" form (like https://k7pisos.example/). - Services: we offer 3 sets of services, each of them composed by three specific services, Namely: * Administration Treasury Accounting Savings * Consulting Legal Technical Regulatory * Mediation Repairs Meetings Delinquency For the sake of structuring, each of the nine services will Have to written description composed of 3 small paragraphs of About 15 words. I Tend to like to Accompany With each of the services related icons / vectors, but feel free to design them as you want. - About us: content not yet defined, but will be a series of bullets / sections in Which We talk about prep or differentiating points. We can include the corporate video presentation here again. - Blog: just a space Where you can see to the blog entries (in Home, probably just show 3/4). - Contact: a fancy contact form, with map, address, telephone, e-mail and opening hours. Just to give it a bit more content, maybe include a catch phrase like "We're looking forward to meeting you!" or something like that. - Estimate: this is the Most Important page in the website (in Addition to the upper part of the Home page). Basically replicate the estimate for the home box, but maybe with a bit more design or extended, Given this is a single page just for that. - Log in: opens a drop-down with user and password (just placeholder, no log in required yet). Regarding colors, we still do not Have a color scheme, so anything in line With the logo is OK. Many thanks in advance, Martin

All ages and genders

Real Estate

Coded - Design and coding required

5+ page

Sans Serif

Must have
• Blank colored background

```html
<!DOCTYPE html>
<html lang="en">
<head>
<meta charset="utf-8">
<title>Portalia720º – Real Estate Services</title>
<link rel="stylesheet" href="https://fonts.googleapis.com/css2?family=Roboto:wght@400;500;700&display=swap">
<style>
  :root {
    --page-bg: #ffffff;
    --ink: #2b2b2b;
    --ink-soft: #555555;
    --accent: #d46f0c;
    --accent-dark: #b85d06;
    --panel: #2a1c12;
    --panel-line: #8a7a6c;
    --field-text: #e9e2da;
    --btn-dark: #241710;
  }
  * { box-sizing: border-box; margin: 0; padding: 0; }
  html, body {
    width: 1200px; height: 855px; overflow: hidden;
    background: var(--page-bg);
    font-family: "Roboto", sans-serif; color: var(--ink);
  }
  .site { position: relative; width: 1200px; height: 855px; }

  /* Header */
  .site-header {
    height: 86px; display: flex; align-items: center;
    padding: 0 60px; background: var(--page-bg);
    box-shadow: 0 2px 6px rgba(0,0,0,.08); position: relative; z-index: 2;
  }
  .brand { display: flex; align-items: center; gap: 10px; text-decoration: none; }
  .brand-mark { width: 14px; height: 14px; background: var(--accent); }
  .brand-name { font-size: 28px; font-weight: 700; color: var(--ink); letter-spacing: -.5px; }
  .main-nav { margin-left: auto; display: flex; align-items: center; gap: 34px; }
  .main-nav a {
    font-size: 12px; font-weight: 500; color: var(--ink); text-decoration: none;
    text-transform: uppercase; padding: 6px 0; letter-spacing: .2px;
  }
  .main-nav a.is-active { color: var(--accent); border-bottom: 2px solid var(--accent); }
  .nav-actions { display: flex; gap: 10px; margin-left: 40px; }
  .btn {
    display: inline-flex; align-items: center; justify-content: center;
    font-family: inherit; font-size: 12px; font-weight: 500; text-transform: uppercase;
    color: #fff; border: 0; border-radius: 2px; height: 34px; padding: 0 22px;
  }
  .btn-login { background: var(--accent); width: 100px; }
  .btn-estimate { background: var(--btn-dark); }

  /* Hero */
  .hero {
    position: absolute; left: 0; top: 86px; width: 1200px; height: 460px;
    background: linear-gradient(180deg, #7c5a9c 0%, #c27aa0 18%, #f0a155 38%, #e07a2c 55%, #9c4a24 75%, #5a2a18 100%);
  }
  .hero-title {
    position: absolute; left: 0; right: 0; top: 200px; text-align: center;
    color: #fff; font-size: 42px; font-weight: 500; line-height: 1.2;
    text-shadow: 0 2px 6px rgba(0,0,0,.45);
  }

  /* Estimate panel */
  .estimate {
    position: absolute; left: 150px; top: 480px; width: 900px; height: 250px;
    background: var(--panel); padding: 26px 40px; z-index: 1;
  }
  .estimate-title { color: var(--accent); font-size: 22px; font-weight: 500; }
  .estimate-rule { height: 1px; background: #4a3a2e; margin: 10px 0 28px; width: 300px; }
  .estimate-form { display: grid; grid-template-columns: 170px 170px 170px 150px 1fr; column-gap: 30px; row-gap: 30px; align-items: end; }
  .field {
    color: var(--field-text); font-size: 12px; padding-bottom: 6px;
    border-bottom: 1px solid var(--panel-line); display: flex; justify-content: space-between;
  }
  .caret { width: 0; height: 0; border-left: 4px solid transparent; border-right: 4px solid transparent; border-top: 5px solid var(--field-text); align-self: center; }
  .switch-row { color: var(--field-text); font-size: 12px; display: flex; justify-content: space-between; align-items: center; padding-bottom: 4px; }
  .switch { width: 26px; height: 12px; border-radius: 6px; background: #d9d2ca; position: relative; }
  .switch::after { content: ""; position: absolute; right: -2px; top: -2px; width: 16px; height: 16px; border-radius: 50%; background: #fff; box-shadow: 0 1px 2px rgba(0,0,0,.4); }
  .btn-submit {
    grid-column: 5; grid-row: 1 / span 2; align-self: center;
    background: var(--accent); height: 58px; width: 92px; font-size: 14px; line-height: 1.1; padding: 0; text-align: center;
  }

  /* Services teaser */
  .section-heading {
    position: absolute; left: 0; right: 0; top: 780px; text-align: center;
    font-size: 30px; font-weight: 400; color: var(--ink);
  }
  .section-heading span { color: var(--accent); font-weight: 500; }
</style>
</head>
<body>
<div class="site">
  <header class="site-header">
    <a class="brand" href="#home"><span class="brand-mark"></span><span class="brand-name">Portalia720º</span></a>
    <nav class="main-nav">
      <a class="is-active" href="#home">Home</a>
      <a href="#services">Services</a>
      <a href="#about">About us</a>
      <a href="#blog">Blog</a>
      <a href="#contact">Contact</a>
    </nav>
    <div class="nav-actions">
      <span class="btn btn-login">Login</span>
      <span class="btn btn-estimate">Free Estimate</span>
    </div>
  </header>

  <section class="hero" role="img" aria-label="Madrid city skyline at sunset with historic rooftops and distant mountains">
    <h1 class="hero-title">Going Above and Beyond<br>to Find Your Next Home</h1>
  </section>

  <section class="estimate">
    <h2 class="estimate-title">Get an Free Estimate</h2>
    <div class="estimate-rule"></div>
    <div class="estimate-form">
      <div class="field">Your Name</div>
      <div class="field">Your Email ID</div>
      <div class="field">Number of Garages <span class="caret"></span></div>
      <div class="switch-row">Swimming Pool <span class="switch"></span></div>
      <span class="btn btn-submit">Submit<br>Now</span>
      <div class="field">Post Code</div>
      <div class="field">Number of Homes <span class="caret"></span></div>
      <div class="field">Number of Stores <span class="caret"></span></div>
      <div class="switch-row">Concierge <span class="switch"></span></div>
    </div>
  </section>

  <h2 class="section-heading">our <span>services</span></h2>
</div>
</body>
</html>
```